Design a certificate of authenticity for artist paintings and prints. This must be very profrssional looking and not school arty. I need it on pdf file. The artist is www.miloprentis.co.uk

```html
<!DOCTYPE html>
<html lang="en">
<head>
<meta charset="utf-8">
<title>Certificate of Authenticity – Milo Prentis</title>
<link rel="stylesheet" href="https://fonts.googleapis.com/css2?family=Crimson+Pro:ital,wght@0,400;0,600;1,400;1,600&display=swap">
<style>
  :root {
    --paper: #eef3f8;
    --paper-deep: #dfe8f1;
    --border-dark: #4e6487;
    --border-mid: #7d92b3;
    --border-light: #b9c7da;
    --frame-line: #5e7497;
    --title: #7f98ad;
    --ink: #1f2630;
    --signature: #5a7192;
    --ribbon-pink: rgba(226, 120, 150, 0.28);
    --ribbon-gold: rgba(240, 205, 120, 0.25);
    --band: rgba(170, 198, 224, 0.45);
  }
  * { margin: 0; padding: 0; box-sizing: border-box; }
  html, body { width: 1200px; height: 748px; overflow: hidden; background: var(--paper); }
  body { font-family: "Crimson Pro", Georgia, serif; color: var(--ink); }

  .certificate { position: relative; width: 1200px; height: 748px; overflow: hidden; background: var(--paper); }

  .border-ornament {
    position: absolute; left: 28px; top: 22px; width: 1144px; height: 704px;
    background: radial-gradient(circle at 50% 50%, var(--border-light) 0%, var(--border-mid) 55%, var(--border-dark) 100%);
  }

  .panel {
    position: absolute; left: 122px; top: 104px; width: 956px; height: 522px;
    background: radial-gradient(ellipse at 50% 45%, #f6f9fc 0%, var(--paper) 55%, var(--paper-deep) 100%);
    border: 3px solid var(--frame-line);
  }
  .panel::before { content: ""; position: absolute; inset: 8px; border: 1px solid var(--frame-line); }
  .panel::after { content: ""; position: absolute; inset: 22px; border: 1px solid var(--border-light); }

  .arch { position: absolute; left: 0; top: 0; width: 1200px; height: 130px; pointer-events: none; }

  .ribbon-decor {
    position: absolute; left: 150px; top: 140px; width: 900px; height: 460px;
    background:
      radial-gradient(ellipse 220px 170px at 14% 45%, var(--ribbon-pink), transparent 70%),
      radial-gradient(ellipse 200px 150px at 26% 30%, var(--ribbon-gold), transparent 70%),
      radial-gradient(ellipse 220px 170px at 84% 50%, var(--ribbon-pink), transparent 70%),
      radial-gradient(ellipse 180px 130px at 72% 40%, var(--ribbon-gold), transparent 70%);
  }

  .band { position: absolute; left: 153px; top: 331px; width: 894px; height: 56px; background: var(--band); }

  .scroll-decor {
    position: absolute; left: 420px; top: 146px; width: 360px; height: 40px;
    background: radial-gradient(ellipse at 50% 50%, rgba(150, 178, 206, 0.55), transparent 70%);
  }

  .brand-name { position: absolute; left: 0; width: 1186px; top: 114px; text-align: center;
    font-size: 20px; line-height: 26px; letter-spacing: 0.08em; color: var(--signature); }

  .meta { position: absolute; font-style: italic; font-size: 13px; line-height: 17px; }
  .meta-issued { left: 185px; top: 188px; }
  .meta-certify { left: 185px; top: 238px; }
  .meta-record { left: 795px; top: 188px; }
  .meta-record span { display: inline-block; }
  .meta-record .label { width: 108px; }

  .title { position: absolute; left: 0; width: 1186px; top: 222px; text-align: center;
    font-size: 46px; line-height: 44px; font-weight: 400; color: var(--title); }

  .statement { position: absolute; left: 160px; width: 866px; top: 391px; text-align: center;
    font-style: italic; font-size: 13px; line-height: 18.5px; white-space: nowrap; }

  .declaration { position: absolute; left: 180px; top: 467px; font-style: italic; font-weight: 600; font-size: 14.5px; }

  .signatory { position: absolute; top: 527px; }
  .signatory .name { font-style: italic; font-size: 30px; line-height: 32px; color: var(--signature); }
  .signatory .role { font-size: 13px; margin-top: 4px; }
  .signatory-left { left: 229px; }
  .signatory-right { right: 237px; text-align: center; }
</style>
</head>
<body>
<main class="certificate">
  <div class="border-ornament" role="img" aria-label="Guilloche security border with repeating blue rosettes and arches"></div>

  <svg class="arch" viewBox="0 0 1200 130" aria-hidden="true">
    <path d="M425 108 Q600 44 775 108" fill="var(--paper)" stroke="var(--frame-line)" stroke-width="3"/>
    <path d="M440 107 Q600 54 760 107" fill="none" stroke="var(--frame-line)" stroke-width="1"/>
  </svg>

  <section class="panel"></section>

  <div class="ribbon-decor" role="img" aria-label="Soft pink and gold guilloche ribbons sweeping across the certificate"></div>
  <div class="band"></div>
  <div class="scroll-decor" role="img" aria-label="Blue filigree scrollwork under the artist name"></div>

  <div class="brand-name">Milo Prentis</div>

  <p class="meta meta-issued">Then under our hand in this day<br>December 6, 2010</p>
  <p class="meta meta-certify">This to certify that</p>
  <p class="meta meta-record">
    <span class="label">Certificate number</span><span>01564</span><br>
    <span class="label">Date of Expiration</span><span>December 31,2011</span>
  </p>

  <h1 class="title">Certificate of<br>Authenticity</h1>

  <p class="statement">Lorem ipsum dolor sit amet, consectetur adipisicing elit, sed do eiusmod tempor incididunt ut labore et dolore magna aliqua. Ut enim ad minim veniam,<br>quis nostrud exercitation ullamco laboris nisi ut aliquip ex ea commodo consequat. Duis aute irure dolor in reprehenderit in voluptate velit esse cillum dolore eu<br>fugiat nulla pariatur. Excepteur sint occaecat cupidatat non proident, sunt in culpa qui officia deserunt mollit anim id est laborum.</p>

  <p class="declaration">Sed ut perspiciatis unde omnis iste natus error sit voluptatem accusantium doloremque laudantium.</p>

  <div class="signatory signatory-left">
    <p class="name">Graham Ellery</p>
    <p class="role">Certification Chairman</p>
  </div>
  <div class="signatory signatory-right">
    <p class="name">Clara Hensley</p>
    <p class="role">Company president</p>
  </div>
</main>
</body>
</html>
```